OurPlume Lifting Hope across a trusted circle

I am looking for a sleek, clean and simple app design. I need also a payment page and offering different packages and payment types.

I would like the color scheme to be black or white very futuristic like the movie q-lantern.

The profile page displaying the picture, as clean and future like as possible.

Share profile options, manage subscription, update profile, help ect….

On the verified page last one, the social media logos are interactive so the user can share their info through the connected social media account.

Target Market(s)

Professionals and individuals.

Industry/Entity Type

Due diligence & background checks verification

Font styles to use
Sans Serif

Colors
0054AA
0677BA
7BADD7
CADEEF
E8F1F8
0094D4
00A9DD
6FCCEA
C7EBF8
E9F6FB
59FF00
82FF00
B8FF75
E3FFCB
F4FFEA

Requirements
Must have
• The ability to add my social media links or log in through the app directly for direct confirmation. After email entered on account sign up they get either a confirmation email or a text through telephone number verification.
Nice to have
• Account creation to add profile picture must take a selfie.

```html
<!DOCTYPE html>
<html lang="en">
<head>
<meta charset="UTF-8">
<title>OurPlume – Create new account</title>
<link rel="stylesheet" href="https://fonts.googleapis.com/css2?family=Roboto:wght@400;500;700&display=swap">
<style>
  :root {
    --bg-top: #2d4257;
    --bg-bottom: #141920;
    --primary: #0054AA;
    --accent: #0094D4;
    --accent-light: #6FCCEA;
    --step-dark: #163a5f;
    --track-dark: #2c4a68;
    --text: #ffffff;
    --text-soft: #d6dde4;
    --text-muted: #9aa3ab;
    --field-border: #7f8a94;
    --note-bg: #232425;
    --note-rule: #4a4c4f;
  }
  * { margin: 0; padding: 0; box-sizing: border-box; }
  html, body { width: 1200px; height: 2619px; overflow: hidden; }
  body {
    font-family: "Roboto", sans-serif;
    color: var(--text);
    background: linear-gradient(180deg, var(--bg-top) 0%, #1e2a37 45%, var(--bg-bottom) 100%);
    position: relative;
  }
  .status-bar { position: absolute; top: 72px; left: 71px; right: 71px; height: 60px; display: flex; justify-content: space-between; align-items: center; }
  .status-time { font-size: 48px; font-weight: 500; }
  .status-icons { display: flex; gap: 18px; align-items: center; }

  .back-button { position: absolute; left: 80px; top: 234px; width: 44px; height: 44px; }

  .page-title { position: absolute; left: 84px; top: 355px; font-size: 97px; font-weight: 500; line-height: 122px; }

  .brand { position: absolute; left: 826px; top: 452px; display: flex; align-items: center; gap: 14px; font-size: 42px; font-weight: 700; color: var(--text); }
  .brand-dot { width: 34px; height: 34px; border-radius: 50%; background: var(--accent); }

  .progress { position: absolute; top: 667px; left: 84px; display: flex; gap: 23px; }
  .progress span { height: 14px; border-radius: 7px; background: var(--accent); }
  .progress .done { width: 193px; }
  .progress .next { width: 32px; }

  .stepper { position: absolute; top: 845px; left: 0; width: 1200px; height: 116px; }
  .step-label { position: absolute; top: 982px; left: 497px; width: 200px; text-align: center; font-size: 36px; color: var(--text-soft); }

  .prompt { position: absolute; top: 1118px; width: 1200px; text-align: center; font-size: 40px; color: var(--text-soft); }

  .field { position: absolute; left: 142px; top: 1252px; width: 916px; height: 158px; border: 3px solid var(--field-border); border-radius: 79px; display: flex; align-items: center; padding-left: 68px; font-size: 45px; color: var(--text-muted); }

  .note { position: absolute; left: 142px; top: 1465px; width: 916px; height: 406px; background: var(--note-bg); border-radius: 26px; }
  .note-head { position: absolute; left: 58px; top: 66px; display: flex; align-items: center; gap: 22px; font-size: 40px; color: var(--text-soft); }
  .note-rule { position: absolute; left: 129px; top: 142px; width: 674px; height: 2px; background: var(--note-rule); }
  .note-body { position: absolute; left: 129px; top: 178px; width: 720px; font-size: 35px; line-height: 52px; color: var(--text-muted); }

  .next-button { position: absolute; left: 103px; top: 2352px; width: 994px; height: 161px; border-radius: 81px; background: var(--primary); display: flex; align-items: center; justify-content: center; gap: 26px; font-size: 48px; font-weight: 700; color: var(--text); }
</style>
</head>
<body>
  <header class="status-bar">
    <span class="status-time">9:41</span>
    <span class="status-icons">
      <svg width="56" height="36" viewBox="0 0 56 36" aria-hidden="true"><g fill="#fff"><rect x="0" y="24" width="10" height="12" rx="2"/><rect x="15" y="17" width="10" height="19" rx="2"/><rect x="30" y="9" width="10" height="27" rx="2"/><rect x="45" y="0" width="10" height="36" rx="2"/></g></svg>
      <svg width="50" height="36" viewBox="0 0 50 36" aria-hidden="true"><g fill="none" stroke="#fff" stroke-width="5" stroke-linecap="round"><path d="M4 12 A30 30 0 0 1 46 12"/><path d="M12 20 A19 19 0 0 1 38 20"/></g><circle cx="25" cy="30" r="5" fill="#fff"/></svg>
      <svg width="82" height="38" viewBox="0 0 82 38" aria-hidden="true"><rect x="2" y="2" width="70" height="34" rx="10" fill="none" stroke="#fff" stroke-width="3"/><rect x="8" y="8" width="58" height="22" rx="5" fill="#fff"/><rect x="76" y="13" width="5" height="12" rx="2" fill="#fff"/></svg>
    </span>
  </header>

  <svg class="back-button" viewBox="0 0 44 44" aria-label="Back"><path d="M30 6 L14 22 L30 38" fill="none" stroke="#fff" stroke-width="6" stroke-linecap="round" stroke-linejoin="round"/></svg>

  <h1 class="page-title">Create new<br>account</h1>

  <div class="brand"><span class="brand-dot"></span>OurPlume</div>

  <div class="progress"><span class="done"></span><span class="next"></span></div>

  <svg class="stepper" viewBox="0 845 1200 116" aria-label="Step 2 of 3">
    <line x1="310" y1="903" x2="500" y2="903" stroke="var(--accent)" stroke-width="4"/>
    <line x1="697" y1="903" x2="910" y2="903" stroke="var(--track-dark)" stroke-width="4"/>
    <circle cx="248" cy="903" r="36" fill="none" stroke="var(--accent-light)" stroke-width="4"/>
    <path d="M228 902 L244 918 L272 884" fill="none" stroke="var(--accent-light)" stroke-width="8" stroke-linecap="round" stroke-linejoin="round"/>
    <circle cx="597" cy="903" r="58" fill="var(--primary)"/>
    <text x="597" y="919" text-anchor="middle" font-family="Roboto, sans-serif" font-size="44" font-weight="700" fill="#fff">2</text>
    <circle cx="958" cy="903" r="32" fill="var(--step-dark)"/>
    <text x="958" y="915" text-anchor="middle" font-family="Roboto, sans-serif" font-size="32" font-weight="500" fill="#4f7aa6">3</text>
  </svg>
  <div class="step-label">User name</div>

  <p class="prompt">Create a unique OurPlume username</p>

  <div class="field">User Name</div>

  <section class="note">
    <div class="note-head">
      <svg width="48" height="48" viewBox="0 0 48 48" aria-hidden="true"><circle cx="24" cy="24" r="22" fill="#e6e6e6"/><rect x="21" y="10" width="6" height="18" rx="3" fill="#232425"/><circle cx="24" cy="35" r="3.5" fill="#232425"/></svg>
      Note that:
    </div>
    <div class="note-rule"></div>
    <p class="note-body">User name must be 3 to 20 characters long. Letters and numbers only. Special characters and spaces are not allowed.</p>
  </section>

  <div class="next-button">Next
    <svg width="28" height="40" viewBox="0 0 28 40" aria-hidden="true"><path d="M8 6 L22 20 L8 34" fill="none" stroke="#fff" stroke-width="5" stroke-linecap="round" stroke-linejoin="round"/></svg>
  </div>
</body>
</html>
```